A2サイズのLED型看板がありその内容の変更です。今回の内容は少し難しいかとおもいますが、宜しくお願い致します。当社は自社ビルで1Fが駐車場で2Fがストレッチ専門店、3~5Fがトレーニングスタジオでトレーニングスタジオの受付は4Fです。A2の中に この2つの内容(パーソナルトレーニングとストレッチ)をあまりごちゃごちゃせずに伝えて頂ければと思っております。
下記をご参考いただければと思います。

法人名は、ミナレクス株式会社
店舗名 4Fトレーニングスタジオナベロ
HP   http://www.k-navelo.jp
http://navelo.net

店舗名 2Fストレッチ専門店 ルミナスカイアークストレッチ
HP  https://www.k-navelo.jp/stretch

写真素材などは別途添付してます。
店舗名/電話番号/ロゴ 受付階
ロゴデータです。
電話番号は、特に表示しなくても良いです。
ビルの何階に何があるのかをわかるようにして頂ければと思います。
やはり、2つあるとごちゃごちゃして少し難しいかと思いますが、トレーニング
とストレッチがわかるような感じと体験についての表記などがあれば良いと
思いますので宜しくお願い致します。
一応、袖にパンフレットをぶら下げておくので興味をもたれた方はパンフを取りたくなるような感じでもお願い致します。
少し、難しくてすみません。。。宜しくお願い致します。

色合いとイメージがピッタリと来ました。ありがとうございました。

この度は、沢山の方からのご提案頂きましてありがとうございました。
また、何かありましたらご提案いただければと思っております。
ありがとうございました。

```html
<!DOCTYPE html>
<html lang="ja">
<head>
<meta charset="utf-8">
<title>ミナレクスビル フロア案内</title>
<link rel="stylesheet" href="https://fonts.googleapis.com/css2?family=Noto+Sans+JP:wght@500;700;900&display=swap">
<style>
:root{
  --red:#e8372f;
  --green:#2e9c48;
  --pink:#e85a8a;
  --ink:#3a3a3a;
  --band:#8a8684;
  --white:#ffffff;
}
*{margin:0;padding:0;box-sizing:border-box}
html,body{width:849px;height:1200px;overflow:hidden;background:#fff}
body{font-family:"Noto Sans JP",sans-serif;color:var(--ink)}
.sign{position:relative;width:849px;height:1200px;background:var(--white);overflow:hidden}

.headline{color:var(--red);font-weight:900;white-space:nowrap}
.headline .line1{position:absolute;left:36px;top:14px;line-height:1.2;letter-spacing:-1px}
.headline .big{font-size:60px}
.headline .small{font-size:44px}
.headline .line2{position:absolute;left:36px;top:96px;font-size:56px;line-height:1.2;letter-spacing:-1px}

.studio-photo{position:absolute;left:34px;top:176px;width:786px;height:394px;border:7px solid var(--green);background:linear-gradient(135deg,#f3efe9,#d9d2c8 55%,#b9b0a6)}
.studio-tags{position:absolute;left:680px;top:188px;display:flex;flex-direction:column;gap:8px}
.studio-tags span{display:block;width:130px;background:var(--white);color:var(--green);border:3px solid var(--green);font-weight:700;font-size:20px;padding:3px 8px;line-height:1.25;white-space:nowrap}
.studio-tags span small{display:block;font-size:13px}
.studio-banner{position:absolute;left:34px;top:500px;height:70px;width:480px;background:var(--green);color:var(--white);display:flex;align-items:center;padding-left:16px;white-space:nowrap;clip-path:polygon(0 0,100% 0,94% 100%,0 100%)}
.studio-banner .floor{font-size:52px;font-weight:900;letter-spacing:-1px;line-height:1}
.studio-banner .name{margin-left:14px;font-size:20px;font-weight:700;line-height:1.25}
.studio-banner .name small{display:block;font-size:13px;font-weight:500}

.trial{position:absolute;left:660px;top:283px;width:172px;height:172px;border-radius:50%;background:var(--red);color:var(--white);display:flex;flex-direction:column;align-items:center;justify-content:center;text-align:center;border:5px solid var(--white);box-shadow:0 0 0 3px var(--red);white-space:nowrap}
.trial .main{font-size:24px;font-weight:900;line-height:1.25}
.trial .sub{font-size:15px;font-weight:700;margin-top:6px;line-height:1.3}

.directory{position:absolute;left:28px;top:660px;width:258px}
.directory .row{display:flex;align-items:center;border-bottom:3px solid var(--ink);white-space:nowrap}
.directory .floors{font-size:26px;font-weight:900;width:64px;line-height:1.3}
.directory .label{font-size:28px;font-weight:900;line-height:1.25}
.directory .label small{display:block;font-size:18px;font-weight:700}
.directory .r1{height:170px}
.directory .r2{height:140px}
.directory .r3{height:110px;border-bottom:none}

.stretch-photo{position:absolute;left:297px;top:580px;width:538px;height:510px;border:7px solid var(--pink);background:linear-gradient(160deg,#f6e6e4,#d8c2bd 60%,#b49c96)}
.stretch-tags{position:absolute;left:318px;top:598px;display:flex;gap:6px}
.stretch-tags span{background:var(--red);color:var(--white);font-size:20px;font-weight:700;padding:2px 12px;white-space:nowrap}
.stretch-banner{position:absolute;left:297px;top:985px;width:500px;height:78px;background:var(--pink);color:var(--white);display:flex;align-items:center;padding-left:16px;white-space:nowrap;clip-path:polygon(0 0,100% 0,94% 100%,0 100%)}
.stretch-banner .floor{font-size:62px;font-weight:900;line-height:1}
.stretch-banner .name{margin-left:12px;font-size:16px;font-weight:700;line-height:1.3}
.stretch-banner .name b{display:block;font-size:24px}

.footer{position:absolute;left:0;top:1096px;width:849px;height:104px;background:var(--band);color:var(--white)}
.footer .corp{position:absolute;top:4px;width:100%;text-align:center;font-size:26px;font-weight:700;letter-spacing:2px;line-height:1.3}
.footer .shop{position:absolute;top:42px;display:flex;flex-direction:column;gap:4px;white-space:nowrap}
.footer .shop .top{display:flex;gap:10px;align-items:center;font-size:17px;font-weight:700;line-height:1.3}
.footer .shop .fl{background:var(--white);color:var(--band);padding:0 10px}
.footer .shop .brand{display:flex;align-items:center;gap:8px;font-size:17px;font-weight:700;background:var(--white);color:var(--ink);padding:2px 12px;align-self:flex-start;line-height:1.4}
.footer .shop .brand i{width:12px;height:12px;border-radius:50%;background:var(--ink);display:inline-block}
.footer .left{left:30px}
.footer .right{left:470px}
</style>
</head>
<body>
<main class="sign">
  <h1 class="headline">
    <span class="line1"><span class="big">ダイエット</span><span class="small">から</span><span class="big">ストレッチ</span><span class="small">まで</span></span>
    <span class="line2">徹底サポート！</span>
  </h1>

  <div class="studio-photo" role="img" aria-label="トレーニングスタジオでダンベルを持つ女性とトレーナーの写真"></div>
  <div class="studio-tags">
    <span><small>短期集中</small>ダイエット</span>
    <span>筋力アップ</span>
  </div>
  <div class="studio-banner">
    <span class="floor">3F-5F</span>
    <span class="name">トレーニングスタジオナベロ<small>※受付は4Fです</small></span>
  </div>

  <div class="trial">
    <span class="main">無料体験や<br>見学もOK！</span>
    <span class="sub">詳しくはこちらを<br>チェック</span>
  </div>

  <nav class="directory" aria-label="フロア案内">
    <div class="row r1"><span class="floors">5F<br>4F<br>3F</span><span class="label">トレーニング<br>スタジオ<small>（受付は4F）</small></span></div>
    <div class="row r2"><span class="floors">2F</span><span class="label">ストレッチ<br>専門店</span></div>
    <div class="row r3"><span class="floors">1F</span><span class="label">駐車場</span></div>
  </nav>

  <div class="stretch-photo" role="img" aria-label="ストレッチ専門店で施術を受ける女性の写真"></div>
  <div class="stretch-tags"><span>肩こり</span><span>首こり</span><span>腰痛</span></div>
  <div class="stretch-banner">
    <span class="floor">2F</span>
    <span class="name">ストレッチ専門店<b>ルミナスカイアークストレッチ</b></span>
  </div>

  <footer class="footer">
    <div class="corp">ミナレクス株式会社</div>
    <div class="shop left">
      <div class="top"><span class="fl">2F</span>ストレッチ専門店</div>
      <span class="brand"><i></i>ルミナスカイアークストレッチ</span>
    </div>
    <div class="shop right">
      <div class="top"><span class="fl">4F</span>トレーニングスタジオナベロ</div>
      <span class="brand"><i></i>ナベロ</span>
    </div>
  </footer>
</main>
</body>
</html>
```